Business Card for Beach theme sports bar called TAVRU

I need a business card designed for our employees, front and back. This will be used by the employees of two business locations to hand out to customers. I've attached the previous business cards we used at one time for a Benwicks (it is now Tavru). Looking for a fresh new card that is elegant but has character.

Target Market(s)

30-60, middle class

Contact Information for Business Card

We are a beach bar and sports bar. I am looking for an elegant business card with the front to have the TAVRU logo. Then on the back I need it to allow a space for employees to write their names and for them to write in their schedule. I have attached our old cards with our old name Benwicks so you can pull everything we need on the cards. one thing is missing is we have another location at 2815 N Willow Crest Rd with a number of 702-418-9351. Since we will use it for both locations it should allow the employee to circle or check mark the bar which they work at.

Font styles to use
Sans Serif

Requirements
Must have
• We are looking for some fresh ideas for the business card. Something that will really stick out to customers when the staff hands them out. Creativity will be looked at positively, but we still want it to look upscale and fun.

```html
<!DOCTYPE html>
<html lang="en">
<head>
<meta charset="utf-8">
<title>Tavru Employee Business Card</title>
<link href="https://fonts.googleapis.com/css2?family=Open+Sans:wght@700;800&display=swap" rel="stylesheet">
<style>
  :root {
    --sand: #e3a23a;
    --cocoa: #5e3617;
    --ink: #111111;
    --paper: #ffffff;
    --backdrop: #f4f1ec;
  }
  * { box-sizing: border-box; margin: 0; padding: 0; }
  html, body { width: 1200px; height: 1200px; overflow: hidden; }
  body {
    background: var(--backdrop);
    font-family: "Open Sans", Arial, sans-serif;
    display: flex;
    flex-direction: column;
    align-items: center;
    justify-content: center;
    gap: 60px;
  }
  .card {
    position: relative;
    width: 900px;
    height: 517px;
    background: var(--sand);
    overflow: hidden;
  }

  /* Front */
  .card-front .shore { position: absolute; inset: 0; }
  .brand {
    position: absolute;
    left: 48px;
    top: 150px;
    display: flex;
    align-items: center;
    gap: 18px;
  }
  .brand-dot {
    width: 34px; height: 34px;
    border-radius: 50%;
    background: var(--ink);
    flex: none;
  }
  .brand-name {
    font-weight: 800;
    font-size: 92px;
    line-height: 1;
    color: var(--ink);
  }
  .employee-name {
    position: absolute;
    left: 494px;
    top: 62px;
    font-weight: 800;
    font-size: 40px;
    color: var(--ink);
    letter-spacing: 0.5px;
  }
  .sun-scene {
    position: absolute;
    left: 504px;
    top: 154px;
    width: 364px;
    height: 364px;
    border-radius: 50%;
    background: var(--cocoa);
  }
  .shell {
    position: absolute;
    left: 54px;
    top: 420px;
    width: 54px;
    height: 66px;
    border-radius: 50% 50% 50% 50% / 60% 60% 40% 40%;
    background: var(--sand);
    transform: rotate(-30deg);
  }

  /* Back */
  .schedule {
    position: absolute;
    left: 58px;
    top: 40px;
    display: grid;
    grid-template-columns: repeat(7, 60px);
    column-gap: 9px;
    row-gap: 8px;
  }
  .day {
    font-weight: 800;
    font-size: 40px;
    color: var(--cocoa);
    text-align: center;
    line-height: 1;
  }
  .day-box {
    height: 56px;
    background: var(--paper);
  }
  .role {
    position: absolute;
    left: 58px;
    width: 474px;
    top: 184px;
    text-align: center;
    font-weight: 800;
    font-size: 40px;
    color: var(--cocoa);
  }
  .name-field {
    position: absolute;
    left: 58px;
    top: 244px;
    width: 474px;
    height: 222px;
    background: var(--paper);
  }
  .locations {
    position: absolute;
    left: 570px;
    top: 40px;
    width: 310px;
    color: var(--ink);
  }
  .locations .brand-name { font-size: 72px; }
  .locations .brand-row {
    display: flex;
    align-items: center;
    justify-content: center;
    gap: 14px;
    height: 240px;
  }
  .locations .brand-dot { width: 26px; height: 26px; }
  .location {
    display: flex;
    align-items: center;
    gap: 14px;
  }
  .location-check {
    flex: none;
    width: 26px;
    height: 26px;
    background: var(--paper);
  }
  .address {
    flex: 1;
    text-align: center;
    font-weight: 700;
    font-size: 17px;
    line-height: 1.3;
  }
  .divider {
    display: block;
    margin: 14px 0 14px 80px;
    width: 150px;
    height: 28px;
  }
</style>
</head>
<body>

  <section class="card card-front" aria-label="Card front">
    <svg class="shore" viewBox="0 0 900 517" preserveAspectRatio="none" aria-hidden="true">
      <path d="M0 392 C 160 360, 330 372, 520 410 C 650 436, 780 440, 900 420 L 900 517 L 0 517 Z" fill="var(--cocoa)"/>
    </svg>
    <div class="brand">
      <span class="brand-dot"></span>
      <span class="brand-name">Tavru</span>
    </div>
    <h1 class="employee-name">EMPLOYEES NAME</h1>
    <div class="sun-scene" role="img" aria-label="Setting sun with palm trees and ocean waves"></div>
    <div class="shell" role="img" aria-label="Seashell"></div>
  </section>

  <section class="card card-back" aria-label="Card back">
    <div class="schedule">
      <span class="day">M</span><span class="day">T</span><span class="day">W</span><span class="day">Th</span><span class="day">F</span><span class="day">Sa</span><span class="day">Su</span>
      <span class="day-box"></span><span class="day-box"></span><span class="day-box"></span><span class="day-box"></span><span class="day-box"></span><span class="day-box"></span><span class="day-box"></span>
    </div>
    <h2 class="role">Bartender</h2>
    <div class="name-field"></div>

    <div class="locations">
      <div class="brand-row">
        <span class="brand-dot"></span>
        <span class="brand-name">Tavru</span>
      </div>
      <div class="location">
        <span class="location-check" aria-label="Check box for this location"></span>
        <p class="address">6140 W Harbor Palm Rd<br>Las Vegas, NV 89147<br>702-530-6128<br>cs@tavrubar.com</p>
      </div>
      <svg class="divider" viewBox="0 0 150 28" aria-hidden="true">
        <rect x="0" y="6" width="150" height="5" fill="var(--cocoa)"/>
        <rect x="0" y="17" width="150" height="5" fill="var(--cocoa)"/>
      </svg>
      <div class="location">
        <span class="location-check" aria-label="Check box for this location"></span>
        <p class="address">2815 N Willow Crest Rd<br>702-418-9351</p>
      </div>
    </div>
  </section>

</body>
</html>
```